Flyerdesign Faltblatt 6 seitiger Wickelfalz - Querformat -  DIN lang
Flyerdesign Faltblatt 6 seitiger Wickelfalz - Querformat - DIN lang
Zielgruppe
Das Geschäft samtweich kosmetik & wellness, bietet Kosmetik und Wellnessbehandlungen an. Zu Werbezwecken soll ein Faltblatt erstellt werden.
Siehe http://kosmetik-mirbental.de
Aufgabenstellung
Ein modernes FLYER-Design zu erstellen.
Faltblatt - 6-seitig Wickelfalz - DIN Lang - Querformat (Gesamtmaße: 63 cm x 10 cm)
Es gibt bereits ein fertiges Webdesign, auf dessen Basis ein passendes Design für einen Wickelfalz-Flyer erstellt werden soll.
Das Faltblatt sollte an meine Homepage angepasst sein. Eine Auswahl von Fotos und das Logo sind als Dateien beigefügt. Ebenfalls beigefügt ist ein Beispiel-Flyer in CS3 Indesign, dessen Abmessungen übernommen werden müssen. In diesem Beispielflyer sind alle Texte hinterlegt, die auch im neu zu erstellenden Flyerdesign verwendet werden müssen.
Die im Beispielflyer vorhandenen 6 Seiten sind in dieser Aufteilung bezogen auf die dort hinterlegten Texte zu übernehmen. Das Datenformat und der Beschnitt sind aus dem Beispiel-Flyer zu übernehmen.
Der neu zu erstellende Flyer ist als Adobe CS3 Indesign Datei zu liefern.

```html
<!DOCTYPE html>
<html lang="de">
<head>
<meta charset="utf-8">
<title>Faltblatt Kosmetik &amp; Wellness</title>
<link href="https://fonts.googleapis.com/css2?family=Raleway:wght@300;400&family=Open+Sans:wght@400;700&family=Tinos&display=swap" rel="stylesheet">
<style>
:root{
  --red:#8c2320;
  --accent:#c8372d;
  --text:#333;
  --pink:#f6dcd3;
  --paper:#fff;
  --sep:#e9e6e4;
}
*{margin:0;padding:0;box-sizing:border-box}
html,body{width:1200px;height:190px;overflow:hidden;background:var(--paper)}
body{position:relative;font-family:'Tinos',serif;color:var(--text);font-size:5.2px;line-height:1.25}
.abs{position:absolute}
.gap{position:absolute;top:0;height:190px;background:var(--sep)}
.band{position:absolute;top:0;height:37px}
.title{position:absolute;font-family:'Raleway',sans-serif;font-weight:300;color:var(--red);font-size:18px;line-height:1;letter-spacing:.5px}
.title.light{color:#fff}
.head{font-family:'Open Sans',sans-serif;font-weight:700;color:var(--red);font-size:4.6px;line-height:1.3}
.sub{font-family:'Open Sans',sans-serif;font-size:4.5px;line-height:1.35;color:#555}
.body{text-align:justify}
.price{position:absolute;display:flex;align-items:center;gap:2px;font-family:'Open Sans',sans-serif;font-size:4.6px;line-height:1;color:var(--accent)}
.ico{width:6px;height:6px;border-radius:50%;background:var(--accent);display:inline-block;margin-left:3px}
.list{list-style:none}
.list li{background:var(--pink);height:8px;line-height:8px;margin-bottom:1.6px;padding:0 4px;font-size:5px;white-space:nowrap}
.plain{list-style:none}
.plain li{line-height:6px;white-space:nowrap}
.photo{position:absolute}
.note{position:absolute;font-family:'Open Sans',sans-serif;font-size:3.6px;line-height:1}
</style>
</head>
<body>

<!-- Kosmetik -->
<div class="band" style="left:0;width:134px;background:linear-gradient(90deg,#fff,#e8e1dd)"></div>
<h1 class="title" style="left:17px;top:14px">KOSMETIK</h1>
<p class="abs body" style="left:17px;top:44px;width:106px">Wer möchte nicht gerne gut und gepflegt aussehen? Dies ist keine Frage des Alters. Abgestimmt auf Ihren Hauttyp bieten wir Ihnen die für Sie optimale Behandlung an.</p>
<p class="abs head" style="left:17px;top:83px;color:var(--text)">Die Gesichtsbehandlungen beinhalten</p>
<ul class="abs list" style="left:17px;top:97px;width:106px">
  <li>Hautanalyse</li><li>Augenbrauenkorrektur</li><li>Reinigungsmaske</li>
  <li>Entfernung von Hautunreinheiten</li><li>Augen- und Lippenpflege</li>
  <li>Wirkstoffampulle</li><li>Tagespflege und Make up</li>
</ul>

<div class="abs" style="left:148px;top:22px;width:115px">
  <p class="head" style="color:var(--text)">Basis Gesicht</p>
  <p class="sub">Auf dem Weg zur erfolgreichen<br>Verbesserung Ihres Hautbildes</p>
  <p class="body">Nach dieser Behandlung fühlt sich Ihre Gesichtshaut glatter und reiner an. Das Ergebnis ist eine subere, klare und ebenmäßige Haut.</p>
</div>
<div class="price" style="left:200px;top:72px"><span class="ico"></span>40 Min<span class="ico"></span>45 Euro</div>
<div class="abs" style="left:148px;top:86px;width:115px">
  <p class="sub">Basis Plus Gesicht</p>
  <p class="sub">Haben Sie oft das Gefühl, dass Ihre Haut spannt?</p>
  <p class="body">Fühlt Sie sich welk und trocken an? Freuen Sie sich auf ein neues samtweiches Hautgefühl. Durch diese Behandlung wird Ihre Haut neu aktiviert, Falten werden sichtbar gemindert. Mit entspannender Gesichtsmassage und Hydromaske.</p>
</div>
<div class="price" style="left:200px;top:166px"><span class="ico"></span>70 Min<span class="ico"></span>80 Euro</div>

<div class="abs" style="left:272px;top:22px;width:115px">
  <p class="head" style="color:var(--text)">MDA Repair</p>
  <p class="sub">Durch Microdermabrasion ein Ergebnis, dass Sie sofort fühlen</p>
  <p class="body">Selbst bei Narben, Hautunreinheiten, großporiger Haut und Falten erhalten Sie sofort sichtbare Erfolge.</p>
</div>
<div class="price" style="left:324px;top:72px"><span class="ico"></span>40 Min<span class="ico"></span>68 Euro</div>
<div class="abs" style="left:272px;top:118px;width:115px">
  <p class="head" style="color:var(--text)">MDA Repair Plus mit Decolleté</p>
  <p class="sub">Für eine strahlende und ebenmäßige Haut</p>
  <p class="body">Die Kombination aus Mikrodermabrasion und Ultraschall macht Ihre Gesichtshaut und Ihr Decolleté strahlender und ebenmäßiger.</p>
</div>
<div class="price" style="left:324px;top:166px"><span class="ico"></span>60 Min<span class="ico"></span>108 Euro</div>

<div class="gap" style="left:401px;width:4px"></div>

<div class="abs" style="left:417px;top:22px;width:115px">
  <p class="head" style="color:var(--text)">Mesoporation</p>
  <p class="sub">Tiefenwirkung garantiert</p>
  <p class="body">Die Mesoporation ist im Bereich der ästhetischen Kosmetik die derzeit effektivste Methode, um Wirkstoffe in tiefere Hautschichten einzuschleusen, ohne die Haut zu verletzen.</p>
</div>
<div class="price" style="left:468px;top:72px"><span class="ico"></span>50 Min<span class="ico"></span>98 Euro</div>
<div class="photo" role="img" aria-label="Foto einer Gesichtsbehandlung mit Mesoporationsgerät" style="left:417px;top:89px;width:97px;height:77px;background:linear-gradient(135deg,#8c7b73,#d9b9a4 55%,#efe3da)"></div>

<!-- Extras / Wellness -->
<div class="band" style="left:548px;width:252px;background:linear-gradient(90deg,#9d918c,#c9bfba 50%,#f4f1ef)"></div>
<h2 class="title light" style="left:562px;top:13px">EXTRAS</h2>
<h2 class="title" style="left:675px;top:13px">WELLNESS</h2>
<ul class="abs plain" style="left:563px;top:47px;width:100px">
  <li>Jugendbehandlungen</li><li>Männerbehandlungen</li><li>Decolleté-Behandlungen</li>
  <li style="margin-top:6px">Wimpernwelle</li><li>Färben Wimpern &amp; Augenbrauen</li><li>Augenbrauenkorrektur</li>
  <li style="margin-top:6px">Enthaarung mit Warmwachs</li><li>Maniküre</li><li>Pediküre</li>
</ul>
<div class="abs" style="left:674px;top:46px;width:106px">
  <p class="body">Entspannung ist ein Thema, dass in unserer hektischen Zeit immer mehr an Bedeutung gewinnt. Die Gedanken an den Alltag loslassen, sich fallen lassen, losgelöst sein und sich gut aufgehoben fühlen.</p>
  <p class="body" style="margin-top:4px">Dieses Gefühl wollen wir unseren Kunden geben.</p>
</div>
<div class="photo" role="img" aria-label="Foto eines hellen Wellnessraums mit Liege" style="left:674px;top:108px;width:106px;height:58px;background:linear-gradient(90deg,#c7c1bb,#efece8 50%,#8a7d72)"></div>

<div class="gap" style="left:800px;width:4px"></div>

<div role="img" aria-label="Heller, verschwommener Blumenhintergrund" style="position:absolute;left:804px;top:0;width:396px;height:190px;background:linear-gradient(160deg,#dcd7d4,#f5f3f2 40%,#fff)"></div>

<div class="abs" style="left:821px;top:22px;width:132px">
  <p class="head">Hot Stone</p>
  <p class="sub" style="color:var(--red)">Erleben Sie eine entspannende Rücken- und Nackenmassage mit erlesenen Ölen – ergänzt um eine wohltuende Kopfmassage</p>
  <p class="body">Vergessen Sie den Alltag und schenken Sie Ihrem Körper neue Lebensenergie. Durch die wohltuende Wärme der Steine und Öle wird diese Massage für Sie zu einem besonderen Erlebnis.</p>
</div>
<div class="price" style="left:872px;top:85px"><span class="ico"></span>40 Min<span class="ico"></span>50 Euro</div>
<div class="abs" style="left:821px;top:100px;width:132px">
  <p class="head">Ayurvedische Ganzkörpermassage*</p>
  <p class="sub" style="color:var(--red)">Nehmen Sie ein Auszeit</p>
  <p class="body">Tauchen Sie ein in eine wunderbare Welt der ayurvedischen Ölmassage und erleben Sie das sanfte Fließen von warmen erlesenen Ölen am eigenen Körper. Diese Entspannungsmassage wirkt Stress abbauend und mobilisierend.</p>
</div>
<div class="price" style="left:872px;top:157px"><span class="ico"></span>50 Min<span class="ico"></span>80 Euro</div>
<p class="note" style="left:973px;top:171px">* Diese Behandlung wird nur für Frauen angeboten.</p>

<div class="abs" style="left:964px;top:22px;width:128px">
  <p class="head">Kopf- und Nackenmassage</p>
  <p class="sub" style="color:var(--red)">Kennen Sie das unglaubliche Gefühl von warmem Öl, dass über Ihre Stirn fließt</p>
  <p class="body">Bei dieser Kopf-, Nacken und Schultermassage können Sie wunderbar entspannen.</p>
</div>
<div class="price" style="left:1016px;top:64px"><span class="ico"></span>30 Min<span class="ico"></span>45 Euro</div>
<div class="photo" role="img" aria-label="Foto einer Kopf- und Nackenmassage" style="left:973px;top:90px;width:89px;height:48px;background:linear-gradient(135deg,#c7a48e,#ead6c8 50%,#a98673)"></div>

<div class="abs" style="left:1106px;top:22px;width:76px">
  <p class="head">Rosentraum*</p>
  <p class="sub" style="color:var(--red)">Zarter Rosenduft betört Sie bei diesem Pflege-Ritual</p>
  <p class="body">Die pflegenden und erlesenen Eigenschaften der Rose machen dieses Ganzkörper-Pflegeritual zu einer wahrhaft königlichen Behandlung. Ein sanftes Ganzkörper-Peeling sorgt für eine verführerisch zarte Haut. Durch die Massage mit warmen Steinen und erlesenen Rosenölen wird diese Behandlung zu einem unvergesslichen Erlebnis.</p>
</div>
<div class="price" style="left:1114px;top:155px"><span class="ico"></span>70 Min<span class="ico"></span>100 Euro</div>

</body>
</html>
```